US company marketing to law enforcement needs brochure design

We have created a new logo and now need to update our printed material. What we really need is a "style" or "template" for how our brochures will look in the future. Enclosed is the brochure draft with the old style and logo. Also enclosed is the new logo. As we are marketing to US law enforcement it is important the the brochure design is strong, powerful and that we are looking experienced and trustworthy. However, we also want to look modern in line with the logo update.

Target Market(s)

Law enforcement

Industry/Entity Type

Marketing

```html
<!DOCTYPE html>
<html lang="en">
<head>
<meta charset="utf-8">
<title>Steadfast Programs – Brochure Cover</title>
<link href="https://fonts.googleapis.com/css2?family=Exo+2:wght@500;700&family=Jost:wght@400&display=swap" rel="stylesheet">
<style>
  :root {
    --navy: #2d3b66;
    --navy-soft: #45558a;
    --white: #ffffff;
    --grey-text: #9d9d9d;
    --grey-band: #a8a6a7;
    --icon-grey: #8f8f8f;
    --rule: #c9ccd6;
    --photo-light: #f6d48e;
    --photo-mid: #d99a3e;
    --photo-dark: #6a3d14;
  }
  html, body { margin: 0; padding: 0; overflow: hidden; background: var(--white); }
  .canvas {
    position: relative;
    width: 1200px;
    height: 776px;
    overflow: hidden;
    background: var(--white);
    font-family: "Exo 2", sans-serif;
  }
  .backdrop { position: absolute; inset: 0; }

  .brand {
    position: absolute;
    display: flex;
    align-items: center;
    gap: 22px;
  }
  .brand-dot { border-radius: 50%; flex: none; }
  .brand-name {
    font-family: "Exo 2", sans-serif;
    font-weight: 500;
    font-size: 40px;
    letter-spacing: 0.2px;
    white-space: nowrap;
  }
  .brand--header { left: 646px; top: 30px; }
  .brand--header .brand-dot { width: 78px; height: 78px; background: var(--white); }
  .brand--header .brand-name { color: var(--white); }
  .brand--contact { left: 69px; top: 437px; }
  .brand--contact .brand-dot { width: 78px; height: 78px; background: var(--navy); }
  .brand--contact .brand-name { color: var(--grey-text); }

  .headline {
    position: absolute;
    left: 600px; width: 600px; top: 330px;
    margin: 0;
    text-align: center;
    color: var(--navy);
    font-weight: 700;
    font-size: 29px;
  }

  .rule {
    position: absolute;
    left: 0; width: 590px; height: 1px;
    background: linear-gradient(90deg, rgba(201,204,214,0) 0%, var(--rule) 25%, var(--rule) 80%, rgba(201,204,214,0) 100%);
  }
  .rule--top { top: 535px; }
  .rule--bottom { top: 706px; }

  .contact-list {
    position: absolute; left: 182px; top: 553px;
    margin: 0; padding: 0; list-style: none;
    font-family: "Jost", sans-serif;
    font-size: 15px; color: var(--navy); line-height: 25px;
  }
  .contact-item { display: flex; align-items: flex-start; gap: 24px; margin-bottom: 14px; }
  .contact-item svg { width: 24px; height: 24px; flex: none; margin-top: 1px; }

  .side-block {
    position: absolute; left: 600px; top: 382px; width: 145px; height: 374px;
    background: var(--navy);
  }
  .programs {
    position: absolute; left: 757px; top: 382px; width: 411px; height: 374px;
    margin: 0; padding: 0; list-style: none;
    background: var(--navy);
  }
  .program {
    height: 73px; line-height: 85px;
    text-align: center; color: var(--white);
    font-weight: 700; font-size: 23px;
    padding-right: 10px;
    border-bottom: 1px solid rgba(255,255,255,0.55);
    margin-right: 52px;
    padding-left: 52px;
    margin-left: 0;
  }
  .program:last-child { border-bottom: none; }
  .edge-strip {
    position: absolute; left: 1168px; top: 382px; width: 32px; height: 374px;
    background: #bdbcbd;
  }
  .edge-dot {
    position: absolute; left: 14px; width: 7px; height: 7px; border-radius: 50%;
    background: var(--navy);
  }
  .footer-band {
    position: absolute; left: 0; top: 756px; width: 1200px; height: 20px;
    background: var(--grey-band);
  }
</style>
</head>
<body>
<div class="canvas">

  <svg class="backdrop" width="1200" height="776" viewBox="0 0 1200 776">
    <defs>
      <clipPath id="header-clip">
        <path d="M0 0 H1200 V100 C960 110 780 175 600 228 C420 282 200 340 0 356 Z"/>
      </clipPath>
      <clipPath id="photo-clip">
        <path d="M600 236 C780 183 960 122 1200 114 V313 H600 Z"/>
      </clipPath>
      <linearGradient id="photo-tone" x1="0" y1="0" x2="1" y2="0.6">
        <stop offset="0" stop-color="var(--photo-dark)"/>
        <stop offset="0.35" stop-color="var(--photo-light)"/>
        <stop offset="0.7" stop-color="var(--photo-mid)"/>
        <stop offset="1" stop-color="var(--photo-dark)"/>
      </linearGradient>
    </defs>

    <g clip-path="url(#header-clip)">
      <rect x="0" y="0" width="1200" height="360" fill="var(--navy)"/>
      <circle cx="148" cy="128" r="226" fill="var(--navy-soft)" opacity="0.75"/>
    </g>

    <g clip-path="url(#photo-clip)" role="img" aria-label="Photo of a wooden judge's gavel resting on its block in warm golden light">
      <rect x="600" y="100" width="600" height="220" fill="url(#photo-tone)"/>
    </g>
    <rect x="600" y="313" width="600" height="4" fill="var(--navy)"/>
  </svg>

  <div class="brand brand--header">
    <span class="brand-dot"></span>
    <span class="brand-name">Steadfast Programs</span>
  </div>

  <h1 class="headline">Comprehensive Offender Programs</h1>

  <div class="brand brand--contact">
    <span class="brand-dot"></span>
    <span class="brand-name">Steadfast Programs</span>
  </div>

  <div class="rule rule--top"></div>

  <ul class="contact-list">
    <li class="contact-item">
      <svg viewBox="0 0 24 24" aria-hidden="true"><path fill="var(--icon-grey)" d="M6.6 3.5c.5-.4 1.2-.3 1.6.2l2 2.7c.4.5.3 1.2-.1 1.6l-1.3 1.2c.9 1.9 2.3 3.4 4.1 4.4l1.3-1.2c.5-.4 1.2-.4 1.6 0l2.6 2.1c.5.4.6 1.1.2 1.6l-1.3 1.6c-.6.7-1.5 1-2.4.8C9.4 17.3 5.9 13.6 4.8 8.1c-.2-.9.1-1.8.8-2.4Z"/></svg>
      <span>(555) 014-7400</span>
    </li>
    <li class="contact-item">
      <svg viewBox="0 0 24 24" aria-hidden="true"><path fill="var(--icon-grey)" d="M12 2a7 7 0 0 0-7 7c0 5 7 13 7 13s7-8 7-13a7 7 0 0 0-7-7Zm0 9.5A2.5 2.5 0 1 1 12 6.5a2.5 2.5 0 0 1 0 5Z"/></svg>
      <span>418 Halvern Street Northeast<br>Washington, DC 20099</span>
    </li>
    <li class="contact-item">
      <svg viewBox="0 0 24 24" aria-hidden="true"><rect x="2.5" y="5.5" width="19" height="13" fill="none" stroke="var(--icon-grey)" stroke-width="1.4"/><path d="M2.5 5.5 12 13l9.5-7.5M2.5 18.5l7-6.5M21.5 18.5l-7-6.5" fill="none" stroke="var(--icon-grey)" stroke-width="1.4"/></svg>
      <span>info@steadfastprograms.example</span>
    </li>
  </ul>

  <div class="rule rule--bottom"></div>

  <div class="side-block"></div>
  <ul class="programs">
    <li class="program">Pre-Trial</li>
    <li class="program">Diversion</li>
    <li class="program">Deferred Prosecution</li>
    <li class="program">Jail Alternative</li>
    <li class="program">Probation</li>
  </ul>
  <div class="edge-strip">
    <span class="edge-dot" style="top:40px"></span>
    <span class="edge-dot" style="top:113px"></span>
    <span class="edge-dot" style="top:187px"></span>
    <span class="edge-dot" style="top:260px"></span>
    <span class="edge-dot" style="top:333px"></span>
  </div>

  <div class="footer-band"></div>
</div>
</body>
</html>
```